Digital Album Cover - Where The Quiet River Bends (Piano & Cello)

HiI would like a digital album coverTitle: "Where The Quiet River Bends (Piano & Cello)"Artist: "Lorcan Pettigrew & The Oduya Priscilla"

• Original creativity
• Copyrighted images

```html
<!DOCTYPE html>
<html lang="en">
<head>
<meta charset="utf-8">
<title>Where The Quiet River Bends (Piano &amp; Cello) — Lorcan Pettigrew &amp; The Oduya Priscilla</title>
<link rel="stylesheet" href="https://fonts.googleapis.com/css2?family=Josefin+Sans:wght@200;300;700&display=swap">
<style>
  :root {
    --paper: #fbf8f2;
    --mint: #d6efe1;
    --sage: #8fbf95;
    --gold: #e8b552;
    --ember: #ef7c3c;
    --blush: #f4d6cf;
    --haze: #f3efe6;
    --ink: #111111;
    --line: rgba(255, 255, 255, 0.95);
    --veil: rgba(255, 255, 255, 0.32);
  }
  * { margin: 0; padding: 0; box-sizing: border-box; }
  html, body {
    width: 1200px;
    height: 1200px;
    overflow: hidden;
    background: var(--paper);
  }
  .cover {
    position: relative;
    width: 1200px;
    height: 1200px;
    overflow: hidden;
  }
  .cover-photo {
    position: absolute;
    inset: 0;
    background:
      radial-gradient(ellipse 28% 34% at 60% 46%, rgba(239,124,60,0.85), rgba(239,124,60,0) 100%),
      radial-gradient(ellipse 30% 40% at 30% 55%, rgba(232,181,82,0.9), rgba(232,181,82,0) 100%),
      radial-gradient(ellipse 25% 30% at 88% 35%, rgba(143,191,149,0.8), rgba(143,191,149,0) 100%),
      radial-gradient(ellipse 40% 30% at 70% 85%, rgba(244,214,207,0.95), rgba(244,214,207,0) 100%),
      linear-gradient(160deg, var(--paper) 0%, var(--mint) 35%, var(--haze) 70%, var(--blush) 100%);
  }
  .cover-graphics {
    position: absolute;
    inset: 0;
  }
  .light-veil { fill: var(--veil); }
  .slash { stroke: var(--line); stroke-width: 11; stroke-linecap: butt; }
  .dot { fill: var(--ink); }
  .album-title {
    font-family: "Josefin Sans", sans-serif;
    font-weight: 200;
    font-size: 44px;
    fill: var(--ink);
  }
  .artist-name {
    font-family: "Josefin Sans", sans-serif;
    font-weight: 700;
    font-size: 15px;
    letter-spacing: 2.4px;
    fill: var(--ink);
  }
</style>
</head>
<body>
  <main class="cover">
    <div class="cover-photo" role="img" aria-label="Sunlit photograph of a young couple embracing, long golden hair, warm orange and mint tones"></div>

    <svg class="cover-graphics" width="1200" height="1200" viewBox="0 0 1200 1200" xmlns="http://www.w3.org/2000/svg">
      <polygon class="light-veil" points="0,0 300,0 960,660 700,920 0,220"/>

      <line class="slash" x1="88" y1="421" x2="652" y2="981"/>
      <line class="slash" x1="249" y1="322" x2="571" y2="644"/>
      <line class="slash" x1="515" y1="394" x2="829" y2="708"/>

      <circle class="dot" cx="600" cy="296" r="9"/>
      <circle class="dot" cx="251" cy="631" r="9"/>
      <circle class="dot" cx="946" cy="631" r="9"/>

      <text class="album-title" x="80" y="1090" textLength="1060" lengthAdjust="spacingAndGlyphs">WHERE THE QUIET RIVER BENDS (PIANO &amp; CELLO)</text>
      <text class="artist-name" x="1140" y="1135" text-anchor="end">LORCAN PETTIGREW &amp; THE ODUYA PRISCILLA</text>
    </svg>
  </main>
</body>
</html>
```